Financial Advisor Brochure to attract new clients

I am launching a new career as a Financial Advisor and a flier that shows what services I offer and why I decided to go back to work at this point in my life. I have a deep desire to help people meet their dreams and believe that a solid financial foundation provides the ability to live your life as you want to and not how you have to. I created a simple flier but know that so much more can be done to catch a persons eye.

Target Market(s)

Entrepeneurs and Woman in all stages of life.

Industry/Entity Type

Financial Advisor

Font styles to use
Sans Serif

Colors
00AB8E
00BBA5
67D7C9
C6EFE9
E9F9F6

Requirements
Must have
• my photo, contact information and Cobaltra Logo

```html
<!DOCTYPE html>
<html lang="en">
<head>
<meta charset="utf-8">
<title>Renata Holloway – Financial Advisor</title>
<link href="https://fonts.googleapis.com/css2?family=Barlow+Condensed:wght@600;700;800&family=Montserrat:wght@400;500;600&display=swap" rel="stylesheet">
<style>
  :root {
    --teal-deep: #00AB8E;
    --teal: #00BBA5;
    --teal-light: #67D7C9;
    --teal-pale: #C6EFE9;
    --teal-mist: #E9F9F6;
    --ink: #3f4644;
    --text: #2b2f2e;
    --white: #ffffff;
    --stage: #cacaca;
    --header-a: #98a09e;
    --header-b: #6f7876;
    --photo-top: #858c8a;
    --photo-bottom: #2a8f7b;
  }
  * { box-sizing: border-box; margin: 0; padding: 0; }
  html, body { width: 1200px; height: 2344px; overflow: hidden; }
  body { background: var(--stage); font-family: "Montserrat", sans-serif; position: relative; }

  .flier {
    position: absolute; left: 50px; top: 395px;
    width: 1100px; height: 1554px;
    background: var(--white);
    box-shadow: -8px 8px 12px rgba(0,0,0,0.35);
    overflow: hidden;
  }
  .header {
    position: absolute; left: 0; top: 0; width: 1100px; height: 733px;
    background: radial-gradient(ellipse at 35% 45%, var(--header-a) 0%, var(--header-b) 85%);
  }
  .portrait {
    position: absolute; left: 500px; top: 0; width: 590px; height: 733px;
    background: linear-gradient(180deg, var(--photo-top) 0%, #7e8785 40%, var(--photo-bottom) 100%);
  }
  .name {
    position: absolute; left: 52px; top: 62px;
    font-family: "Barlow Condensed", sans-serif; font-weight: 800;
    font-size: 78px; line-height: 1; color: var(--ink); letter-spacing: 0.5px;
  }
  .title {
    position: absolute; left: 52px; top: 146px;
    font-family: "Barlow Condensed", sans-serif; font-weight: 700;
    font-size: 53px; line-height: 1; color: var(--white);
  }
  .label {
    position: absolute; left: 52px;
    font-family: "Barlow Condensed", sans-serif; font-weight: 700;
    font-size: 27px; line-height: 1; color: var(--teal-light); letter-spacing: 0.5px;
  }
  .profile-text {
    position: absolute; left: 52px; top: 278px; width: 440px;
    font-size: 18px; font-weight: 600; line-height: 22px; color: var(--white);
  }
  .cta {
    position: absolute; left: 52px; top: 391px; height: 40px; padding: 0 18px;
    background: var(--white); border-radius: 6px;
    font-family: "Barlow Condensed", sans-serif; font-weight: 700;
    font-size: 28px; line-height: 40px; color: var(--teal-deep);
  }
  .phone {
    position: absolute; left: 52px; top: 442px; display: flex; align-items: center; gap: 14px;
    font-family: "Barlow Condensed", sans-serif; font-weight: 800;
    font-size: 44px; line-height: 1; color: var(--white);
  }
  .contact-value {
    position: absolute; left: 52px; font-size: 19px; font-weight: 500; color: var(--white);
  }

  .story {
    position: absolute; left: 54px; top: 770px; width: 410px;
    font-size: 18.5px; line-height: 22.3px; color: var(--text);
    text-align: justify;
  }
  .story p + p { margin-top: 22px; }

  .services { position: absolute; left: 540px; top: 756px; width: 540px; }
  .services-heading {
    font-family: "Barlow Condensed", sans-serif; font-weight: 700;
    font-size: 38px; line-height: 1; color: var(--ink); margin-bottom: 16px;
  }
  .service + .service { margin-top: 26px; }
  .service-tag {
    display: inline-block; background: var(--teal-deep); color: var(--white);
    font-family: "Barlow Condensed", sans-serif; font-weight: 700;
    font-size: 28px; line-height: 34px; padding: 0 14px; border-radius: 6px;
    margin-bottom: 8px; vertical-align: top;
  }
  .service ul { list-style: none; }
  .service li {
    position: relative; padding-left: 20px;
    font-size: 18px; line-height: 22px; color: var(--text); margin-bottom: 6px;
  }
  .service li::before {
    content: ""; position: absolute; left: 2px; top: 7px;
    width: 9px; height: 9px; border-radius: 50%; background: var(--teal-deep);
  }
  .footer-band {
    position: absolute; left: 0; bottom: 0; width: 1100px; height: 18px; background: var(--teal);
  }
</style>
</head>
<body>
  <article class="flier">
    <header class="header">
      <div class="portrait" role="img" aria-label="Portrait photo of the advisor"></div>
      <h1 class="name">RENATA HOLLOWAY</h1>
      <div class="title">Financial Advisor</div>
      <div class="label" style="top:244px">PROFILE</div>
      <p class="profile-text">Passionate about helping empower you with knowledge to make informed financial decisions throughout all of life’s stages and help you achieve your goals.</p>
      <div class="cta">CALL FOR AN APPOINTMENT</div>
      <div class="phone">
        <svg width="36" height="36" viewBox="0 0 36 36" aria-hidden="true">
          <path d="M9 4 L14 11 L11 15 Q14 21 20 24 L24 21 L31 26 L28 32 Q12 32 4 10 Z" fill="none" stroke="#fff" stroke-width="3" stroke-linejoin="round"/>
          <path d="M21 9 Q26 10 27 15" fill="none" stroke="#fff" stroke-width="2.5" stroke-linecap="round"/>
          <path d="M22 3 Q32 5 33 14" fill="none" stroke="#fff" stroke-width="2.5" stroke-linecap="round"/>
        </svg>
        <span>407-555-0186</span>
      </div>
      <div class="label" style="top:512px">EMAIL:</div>
      <div class="contact-value" style="top:552px">renata.holloway@cobaltrawealthalliance.com</div>
      <div class="label" style="top:597px">WEBSITE:</div>
      <div class="contact-value" style="top:631px">www.cobaltrawealthalliance.com</div>
    </header>

    <section class="story">
      <p>As a business owner, wife, and mother of two teenagers, I understand the struggles you face juggling your personal, business, and financial life.</p>
      <p>I grew up in a home where my parents had opposing money habits. My Dad was a big spender and mom was a saver. Through the years, I saw how my mom’s consistent savings grew while Dad’s style led to many financial ups and downs. This made a huge impression on me and sparked my contin&shy;ued interest in all things finance.</p>
      <p>Having an entrepreneurial personality and ability to explain concepts in a relatable manner has provided me with many oppor&shy;tunities. In 2018, After decades of running a sales agency, I sold my company to spend time with my kids and family but my inter&shy;est in Finance never waned. Now that our kids are thriving teenagers, I started a new career as a licensed Financial Advisor with a heart to help you achieve your financial dreams.</p>
      <p>The financial world is changing rapidly, and it can be confusing on how to maneuver through these times. My goal is to pull out the emotions that cloud judgement and help you make better decisions with your long-range goals in mind</p>
    </section>

    <section class="services">
      <h2 class="services-heading">Financial planning services offered:</h2>
      <div class="service">
        <span class="service-tag">Transition Planning</span>
        <ul><li>Divorce planning.</li><li>Strategy and guidance pre, during, and postdivorce</li></ul>
      </div>
      <div class="service">
        <span class="service-tag">Retirement planning</span>
        <ul><li>Current portfolio analysis</li><li>Timeline asset and income planning</li><li>Tax and estate review and projections</li></ul>
      </div>
      <div class="service">
        <span class="service-tag">Real estate acquisition or sale</span>
        <ul><li>Acquisition or dissolution of real estate.<br>Individual or portfolio</li></ul>
      </div>
      <div class="service">
        <span class="service-tag">Business sale or purchase:</span>
        <ul><li>Company valuations</li><li>Tax impact analysis</li><li>Strategy implementation for funds<br>received from sale.</li></ul>
      </div>
      <div class="service">
        <span class="service-tag">Estate planning</span>
        <ul><li>Strategies for creating future generational wealth.</li></ul>
      </div>
      <div class="service">
        <span class="service-tag">New Investors:</span>
        <ul><li>Assistance in opening investment and<br>retirement acc</li></ul>
      </div>
    </section>

    <div class="footer-band"></div>
  </article>
</body>
</html>
```